Two Rollup Banners Promoting Trade Association

UPDATE: Please do not recycle the prior designs we've had. I am looking for creativity and a new look. Otherwise, I would use the prior designers to just update their work.
I need two 48"x79" Pull Up Retractable Banners Designed.
One promotes the benefits of membership in the Attainable Dwelling Partners Guild. The second promotes ADPG's role in the affordable housing ecosystem.
The content for each is attached. I'm also providing examples of two banners we recently created for our 30th Anniversary as well as some photos of our members if you choose to use them (although it's not necessary - just providing them as an option).
The banners don't have to mimic the ones we did for our 30th Anniversary. I'm simply providing them as examples of designs that meet the look and feel of our brand.
I've also provided our brand guidelines and the specs for the banner.
Updates
All,
We are looking for clean, modern, streamlined designs. No clip art. No waves. Don’t bury the message in the graphics.
Please keep that in mind as you submit designs.
Look and feel
Each slider illustrates characteristics of the customer's brand and the style your logo design should communicate.

```html
<!DOCTYPE html>
<html lang="en">
<head>
<meta charset="utf-8">
<title>ADPG Rollup Banners</title>
<link rel="stylesheet" href="https://fonts.googleapis.com/css2?family=Fira+Sans:wght@400;500;700&family=Roboto:wght@400&family=Noto+Serif:wght@400&display=swap">
<style>
  :root{
    --orange:#e87b3e;
    --orange-bright:#f05a12;
    --orange-soft:#ec7a3c;
    --slate:#5f6a73;
    --slate-block:#6a7580;
    --ink:#4b545c;
    --paper:#ffffff;
    --stage:#ffffff;
  }
  *{box-sizing:border-box;margin:0;padding:0}
  html,body{width:1200px;height:993px;overflow:hidden;background:var(--stage)}
  body{position:relative;font-family:"Fira Sans",sans-serif;color:var(--ink)}

  .banner-number{position:absolute;top:8px;width:60px;text-align:center;font-family:"Roboto",sans-serif;font-size:52px;font-weight:400;color:var(--orange);line-height:1}
  .banner-number--two{left:288px}
  .banner-number--one{left:877px}

  .banner{position:absolute;width:516px;height:862px;background:var(--paper);overflow:hidden;
    box-shadow:0 0 40px rgba(240,140,80,.28),0 6px 18px rgba(0,0,0,.08)}
  .banner--mission{left:61px;top:67px}
  .banner--membership{left:619px;top:64px}
  .banner__band{position:absolute;left:0;top:0;width:100%;height:31px;background:var(--orange)}

  .brand{position:absolute;left:0;top:73px;width:100%;height:74px;display:flex;align-items:center;justify-content:center;gap:14px}
  .brand__mark{width:44px;height:44px;background:var(--orange-bright)}
  .brand__short{font-family:"Fira Sans",sans-serif;font-weight:500;font-size:74px;line-height:1;color:var(--slate);letter-spacing:-1px}
  .brand__rule{width:1px;height:74px;background:#b9bec2}
  .brand__full{font-family:"Fira Sans",sans-serif;font-weight:500;font-size:14px;line-height:16px;color:#8d9499;letter-spacing:1px;text-transform:uppercase}

  .line{position:absolute;left:0;width:100%;text-align:center;white-space:nowrap}
  .headline{font-weight:700;color:var(--orange-bright);font-size:34px;line-height:1}
  .headline--wide{font-size:25.5px;color:var(--orange-soft)}
  .subhead{font-weight:500;color:var(--orange-soft);font-size:22px;line-height:1}
  .section-title{font-weight:700;color:var(--orange-bright);font-size:15px;line-height:1}
  .section-title--large{font-size:22.5px;color:var(--orange-soft)}
  .fact{font-size:10px;font-weight:500;color:var(--ink);line-height:1}
  .fact--stat{font-size:11px}

  .pillars{position:absolute;left:115px;top:273px;list-style:none}
  .pillars li{position:relative;padding-left:13px;font-size:11.5px;font-weight:500;line-height:18px;color:var(--ink)}
  .pillars li::before{content:"";position:absolute;left:0;top:6px;width:6px;height:6px;border-radius:50%;background:var(--slate)}

  .benefits{position:absolute;left:38px;top:269px;list-style:none}
  .benefits li{font-size:15px;font-weight:500;line-height:18.2px;color:var(--ink);white-space:nowrap}
  .benefits .benefits__verb{color:var(--orange-soft)}

  .community{position:absolute;left:38px;top:447px;font-family:"Roboto",sans-serif;font-size:12px;line-height:13.5px;color:var(--ink);width:440px}

  .tile{position:absolute}
  .tile--photo{background:linear-gradient(135deg,#8a7a6c 0%,#b8a796 45%,#6f6a68 100%)}
  .tile--photo.tile--room{background:linear-gradient(160deg,#b9b4ad 0%,#8f8a86 50%,#53575c 100%)}
  .tile--slate{background:var(--slate-block)}
  .tile--orange{background:var(--orange)}

  .cta{font-weight:700;font-size:23px;color:var(--orange-bright);line-height:1}
  .url{font-family:"Roboto",sans-serif;font-size:19px;color:var(--ink);line-height:1}
</style>
</head>
<body>

<div class="banner-number banner-number--two">2</div>
<div class="banner-number banner-number--one">1</div>

<!-- Banner 2: role in the ecosystem -->
<section class="banner banner--mission">
  <div class="banner__band"></div>
  <div class="brand">
    <span class="brand__mark"></span>
    <span class="brand__short">ADPG</span>
    <span class="brand__rule"></span>
    <span class="brand__full">Attainable<br>Dwelling<br>Partners<br>Guild</span>
  </div>

  <div class="line headline" style="top:183px">WHERE LIHTC INVESTING</div>
  <div class="line headline" style="top:219px">EXCELLENCE BEGINS</div>

  <ul class="pillars">
    <li>Setting Industry Standards &amp; Best Practices</li>
    <li>Building Community Through Candid Exchange</li>
    <li>Promoting the Investor Perspective</li>
    <li>Fostering Collaboration Across the Ecosystem</li>
  </ul>

  <div class="line section-title" style="top:371px">30 YEARS OF IMPACT</div>
  <div class="line fact" style="top:416px">Industry-Adopted Standards in Underwriting,</div>
  <div class="line fact" style="top:429px">Asset Management, Risk Rating &amp; More</div>
  <div class="line fact fact--stat" style="top:451px">4 Million Rental Homes Created</div>
  <div class="line fact fact--stat" style="top:466px">9.28 Million Low-Income Households Served</div>

  <div class="tile tile--photo tile--room" style="left:0;top:519px;width:125px;height:126px" role="img" aria-label="Two members talking at a conference table"></div>
  <div class="tile tile--slate" style="left:129px;top:519px;width:129px;height:126px"></div>
  <div class="tile tile--photo" style="left:259px;top:519px;width:126px;height:126px" role="img" aria-label="Members in discussion at a meeting table"></div>
  <div class="tile tile--photo tile--room" style="left:390px;top:519px;width:125px;height:126px" role="img" aria-label="Two members in conversation"></div>
  <div class="tile tile--photo tile--room" style="left:0;top:652px;width:254px;height:126px" role="img" aria-label="Roundtable session with attendees"></div>
  <div class="tile tile--orange" style="left:259px;top:652px;width:129px;height:126px"></div>
  <div class="tile tile--photo" style="left:390px;top:652px;width:125px;height:126px" role="img" aria-label="Speaker addressing the room with a microphone"></div>

  <div class="line cta" style="top:799px">JOIN US TODAY</div>
  <div class="line url" style="top:825px">WWW.ADPG.ORG</div>
</section>

<!-- Banner 1: membership benefits -->
<section class="banner banner--membership">
  <div class="banner__band"></div>
  <div class="brand">
    <span class="brand__mark"></span>
    <span class="brand__short">ADPG</span>
    <span class="brand__rule"></span>
    <span class="brand__full">Attainable<br>Dwelling<br>Partners<br>Guild</span>
  </div>

  <div class="line headline headline--wide" style="top:190px">LIHTC INVESTOR-ONLY COMMUNITY</div>
  <div class="line subhead" style="top:227px;left:-9px">WHERE INVESTORS</div>

  <ul class="benefits">
    <li><span class="benefits__verb">Network:</span>&nbsp; Peer Groups &amp; Forums</li>
    <li><span class="benefits__verb">Learn:</span> Conferences &amp; Webinars</li>
    <li><span class="benefits__verb">Share:</span> Candid Investor-Only Exchange</li>
    <li><span class="benefits__verb">Shape:</span> Industry Standards &amp; Best Practices</li>
    <li><span class="benefits__verb">Grow:</span> Professional Development &amp; Emerging Leaders Program</li>
  </ul>

  <div class="line section-title section-title--large" style="top:395px">OUR COMMUNITY</div>
  <p class="community">60+ Investor Firms 1,000+ Industry Professionals Banks (Large &amp; Small), Insurance Companies, Economic Investors</p>

  <div class="tile tile--photo" style="left:0;top:519px;width:125px;height:126px" role="img" aria-label="Member speaking with a microphone"></div>
  <div class="tile tile--slate" style="left:129px;top:519px;width:129px;height:126px"></div>
  <div class="tile tile--photo tile--room" style="left:259px;top:519px;width:125px;height:126px" role="img" aria-label="Members in lively table discussion"></div>
  <div class="tile tile--photo tile--room" style="left:390px;top:519px;width:125px;height:126px" role="img" aria-label="Two members in conversation"></div>
  <div class="tile tile--photo tile--room" style="left:0;top:650px;width:255px;height:126px" role="img" aria-label="Attendees seated at a conference session"></div>
  <div class="tile tile--orange" style="left:258px;top:648px;width:129px;height:126px"></div>
  <div class="tile tile--photo tile--room" style="left:390px;top:650px;width:125px;height:124px" role="img" aria-label="Two members talking at a conference table"></div>

  <div class="line cta" style="top:799px">JOIN US TODAY</div>
  <div class="line url" style="top:825px">WWW.ADPG.ORG</div>
</section>

</body>
</html>
```